Shopify store for hemp

I need a store designed for Shopify for my hemp company. I currently have a brick and mortar store, but we are looking to get some business online as well. I will upload our logo for reference. We want a clean look. Categories like THCA Flower, Concentrates, Vapes, Edibles would be nice so that we can put individual products under them. I want something about all products being third-party lab tested. All products are sourced in the United States.
Updates

Target Market(s)

Former customers who live in different areas and signed up for our marketing list.

Industry/Entity Type

Hemp/Cannabis

Coding

Coded - Design and coding required

Number of Pages Required

1 page

Requirements
Must have
• Clean feel

```html
<!DOCTYPE html>
<html lang="en">
<head>
<meta charset="utf-8">
<title>Ridgeline Hemp Co. – Store</title>
<link href="https://fonts.googleapis.com/css2?family=Montserrat:wght@500;600;700;800;900&family=Inter:wght@400;500;600&display=swap" rel="stylesheet">
<style>
:root{
  --blue:#4a8fbf;
  --green:#4d8a4a;
  --green-dark:#2f6b2e;
  --green-soft:#8fd98b;
  --mint:#eaf5ea;
  --ink:#151515;
  --line:#c9c9c9;
  --white:#fff;
}
*{box-sizing:border-box;margin:0;padding:0}
html,body{width:1200px;height:4225px;overflow:hidden}
body{font-family:"Inter",sans-serif;color:var(--ink);background:var(--white);position:relative}
.wrap{width:902px;margin:0 auto;position:relative}
h2{font-family:"Montserrat",sans-serif;font-weight:800;text-transform:uppercase}

/* top bar */
.topbar{height:30px;background:var(--blue);color:#fff;font-size:11px;display:flex;justify-content:center;align-items:center}
.topbar span{display:flex;align-items:center;gap:8px;padding:0 40px;border-right:1px solid rgba(255,255,255,.6)}
.topbar span:last-child{border:none}
.topbar i{width:12px;height:12px;border-radius:50%;border:1.5px solid #fff;display:inline-block}

/* header */
.header{height:145px;position:relative;z-index:5;background:#fff}
.logo{position:absolute;left:146px;top:-4px;width:196px;height:196px;border-radius:50%;background:#fff;display:flex;align-items:center;justify-content:center;box-shadow:0 2px 6px rgba(0,0,0,.08)}
.logo-name{width:160px;height:160px;border-radius:50%;background:var(--green);display:flex;align-items:center;justify-content:center;text-align:center;color:#fff;font-family:"Montserrat",sans-serif;font-weight:700;font-size:18px;line-height:1.3}
.search{position:absolute;left:598px;top:32px;width:275px;height:38px;border:1.5px solid #777;font-size:12px;color:#666;padding:11px 14px}
.search svg{position:absolute;right:12px;top:10px}
.icons{position:absolute;left:910px;top:68px;display:flex;gap:22px}
.cart-badge{position:absolute;right:-8px;top:-8px;width:14px;height:14px;border-radius:50%;background:var(--green);color:#fff;font-size:8px;text-align:center;line-height:14px}
.nav{position:absolute;left:410px;top:126px;display:flex;align-items:center;gap:28px;font-family:"Montserrat",sans-serif;font-size:13px;font-weight:500;line-height:16px}
.nav a{color:var(--ink);text-decoration:none}
.nav a.active{background:var(--green);color:#fff;padding:8px 12px;border-radius:4px}

/* hero */
.hero{height:556px;position:relative;background:radial-gradient(ellipse at 70% 40%,#8d8a3e 0%,#56652f 35%,#2d3a26 70%,#1e231c 100%)}
.hero-copy{position:absolute;left:149px;top:105px;color:#fff}
.hero-copy h1{font-family:"Montserrat",sans-serif;font-weight:900;font-size:56px;line-height:64px;text-transform:uppercase}
.hero-copy h1 em{font-style:normal;color:var(--blue)}
.hero-copy p{font-family:"Montserrat",sans-serif;font-weight:600;font-size:20px;line-height:30px;margin-top:26px}
.btn-soft{display:inline-block;background:var(--green-soft);color:var(--green-dark);font-family:"Montserrat",sans-serif;font-weight:800;font-size:18px;padding:15px 28px;border-radius:6px;margin-top:32px;text-transform:uppercase}
.dots{position:absolute;left:560px;top:512px;display:flex;gap:14px}
.dots b{width:10px;height:10px;border-radius:50%;background:#fff}
.dots b:first-child{background:var(--blue)}

/* categories */
.cats{height:618px;text-align:center;padding-top:48px}
.cats h2{font-size:34px}
.sub{font-size:16px;margin-top:12px;color:#222}
.cat-row{display:flex;gap:14px;margin-top:36px}
.cat{width:215px}
.cat .ph{height:280px;border-radius:10px}
.cat p{font-weight:600;font-size:16px;margin-top:22px}
.btn-row{display:flex;justify-content:center;gap:18px;margin-top:38px}
.btn-line{border:2px solid var(--green);color:var(--green);border-radius:10px;font-family:"Montserrat",sans-serif;font-weight:700;font-size:13px;padding:14px 20px;text-transform:uppercase}

/* standards */
.standards{height:271px;background:var(--blue);color:#fff;text-align:center;padding-top:46px}
.standards h2{font-size:28px}
.std-row{display:flex;justify-content:space-between;width:880px;margin:30px auto 0}
.std{width:160px;font-family:"Montserrat",sans-serif;font-weight:700;font-size:14px;line-height:20px;text-transform:uppercase}
.std svg{display:block;margin:0 auto 10px}

/* products */
.products{height:729px;text-align:center;padding-top:56px}
.products h2{font-size:34px}
.tabs{display:flex;justify-content:center;gap:28px;margin-top:44px;font-weight:600;font-size:14px}
.tabs span.on{background:var(--green);color:#fff;padding:2px 10px;border-radius:12px}
.prod-row{display:flex;gap:13px;margin-top:44px;align-items:flex-start}
.prod{width:215px;height:378px;border:1.5px solid var(--line);border-radius:10px;position:relative;padding-top:30px}
.prod.hot{height:410px;background:var(--mint);border-color:#9dbb9b}
.prod .ph{width:150px;height:200px;margin:0 auto;border-radius:8px}
.stars{color:var(--green);font-size:14px;letter-spacing:2px;margin-top:18px}
.prod p{font-size:13px;line-height:19px;margin-top:6px;padding:0 26px}
.price{font-weight:700;font-size:16px;margin-top:12px}
.buy{display:inline-block;background:var(--green);color:#fff;font-size:12px;font-weight:600;padding:6px 16px;border-radius:14px;margin-top:10px}
.mini{position:absolute;top:14px}
.arrow{position:absolute;top:2045px;width:32px;height:32px;border:1.5px solid var(--green);display:flex;align-items:center;justify-content:center}

/* sustainability */
.sustain{height:516px;background:linear-gradient(180deg,#33464e 0%,#3f5a4c 50%,#5e7258 100%);position:relative;color:#fff}
.sustain .ph{position:absolute;left:150px;top:78px;width:344px;height:390px;border-radius:12px}
.sustain-copy{position:absolute;left:556px;top:78px;width:490px}
.sustain-copy h2{font-size:32px}
.rule{width:40px;height:2px;background:#fff;margin:16px 0 28px}
.sustain-copy p{font-size:16px;line-height:24px}

/* stories */
.stories{height:660px;text-align:center;padding-top:75px}
.stories .kicker{font-size:20px}
.stories h2{font-size:32px;margin-top:12px}
.story-row{display:flex;gap:13px;margin-top:36px}
.story{width:217px;height:398px;border-radius:10px;text-align:left}
.quote{background:var(--mint);padding:26px 28px}
.quote .qm{font-family:"Montserrat",sans-serif;font-size:56px;color:var(--green);line-height:40px;font-weight:500}
.quote p{font-size:11px;line-height:18px;margin-top:20px}
.who{display:flex;align-items:center;gap:12px;margin-top:20px;font-size:11px;line-height:16px}
.who i{width:38px;height:38px;border-radius:50%;background:#6b5a48}

/* newsletter */
.news{height:338px;background:linear-gradient(135deg,#3b7f3a,#5a9b4e 50%,#3a7a38);color:#fff;text-align:center;padding-top:78px}
.news h2{font-size:32px}
.news p{font-size:20px;font-weight:500;margin-top:8px}
.field{width:736px;height:58px;border:2.5px solid #fff;border-radius:8px;margin:40px auto 0;position:relative;text-align:left;padding:16px 22px;font-size:14px;font-weight:500}
.field b{position:absolute;right:8px;top:8px;background:#fff;color:var(--green);border-radius:6px;font-family:"Montserrat",sans-serif;font-weight:800;font-size:17px;padding:8px 28px}

/* footer */
.footer{height:362px;position:relative}
.f-logo{position:absolute;left:150px;top:16px;width:192px;height:192px;border-radius:50%;background:var(--green);color:#fff;display:flex;align-items:center;justify-content:center;text-align:center;font-family:"Montserrat",sans-serif;font-weight:700;font-size:20px;line-height:1.3}
.f-col{position:absolute;top:50px;font-size:12px;line-height:20px}
.f-col h4{font-family:"Montserrat",sans-serif;font-weight:800;font-size:14px;margin-bottom:14px}
.f-line{display:flex;gap:16px;margin-bottom:18px;font-weight:500}
.socials{display:flex;gap:5px}
.socials i{width:24px;height:24px;border-radius:50%;background:var(--blue)}
.enquire{display:inline-block;background:var(--green);color:#fff;font-family:"Montserrat",sans-serif;font-weight:800;font-size:18px;padding:14px 28px;border-radius:6px;margin-top:40px}
.copy{position:absolute;left:149px;right:149px;top:270px;border-top:1px solid #bbb;text-align:center;padding-top:28px;font-size:12px}
</style>
</head>
<body>

<div class="topbar">
  <span><i></i>3500+ Products To Choose From</span>
  <span><i></i>Free Doctor Consultations</span>
  <span><i></i>Hemp products for Everyone</span>
  <span><i></i>24/7 Support</span>
</div>

<header class="header">
  <div class="logo"><div class="logo-name">Ridgeline<br>Hemp Co.</div></div>
  <div class="search">Search
    <svg width="16" height="16" viewBox="0 0 16 16" fill="none" stroke="#333" stroke-width="1.6"><circle cx="7" cy="7" r="5"/><path d="M11 11l4 4"/></svg>
  </div>
  <div class="icons">
    <svg width="26" height="26" viewBox="0 0 26 26" fill="none" stroke="#111" stroke-width="2"><circle cx="13" cy="13" r="11"/><circle cx="13" cy="10" r="4"/><path d="M6 20c2-4 12-4 14 0"/></svg>
    <svg width="28" height="26" viewBox="0 0 28 26" fill="none" stroke="#111" stroke-width="2"><path d="M14 23S3 16 3 9a5.5 5.5 0 0111-2 5.5 5.5 0 0111 2c0 7-11 14-11 14z"/></svg>
    <span style="position:relative"><svg width="28" height="26" viewBox="0 0 28 26" fill="none" stroke="#111" stroke-width="2"><path d="M2 3h4l3 14h14l3-10H8"/><circle cx="11" cy="22" r="2"/><circle cx="21" cy="22" r="2"/></svg><span class="cart-badge">0</span></span>
  </div>
  <nav class="nav">
    <a class="active">HOME</a><a>ABOUT US</a><a>CATEGORIES</a><a>PRODUCTS</a><a>BLOG</a><a>SHOP</a><a>CONTACT US</a>
  </nav>
</header>

<section class="hero" role="img" aria-label="Close-up photo of a frosty hemp flower bud with green leaves">
  <div class="hero-copy">
    <h1>Experience<br>Pure <em>THCA</em><br><em>Flower</em></h1>
    <p>Hand-selected strains, crafted<br>for quality and freshness.</p>
    <span class="btn-soft">Shop Now</span>
  </div>
  <div class="dots"><b></b><b></b><b></b><b></b></div>
</section>

<section class="cats">
  <div class="wrap">
    <h2>Categories</h2>
    <p class="sub">Explore our hand-selected strains tailored to every lifestyle</p>
    <div class="cat-row">
      <div class="cat"><div class="ph" role="img" aria-label="Photo of dried hemp flower buds" style="background:linear-gradient(160deg,#6d7a44,#3d4a2a)"></div><p>THCA Flower</p></div>
      <div class="cat"><div class="ph" role="img" aria-label="Photo of golden concentrate in a glass jar with a dab tool" style="background:linear-gradient(160deg,#c79a6a,#8a5a36)"></div><p>Concentrates</p></div>
      <div class="cat"><div class="ph" role="img" aria-label="Photo of a hemp vape liquid bottle beside a hemp leaf" style="background:linear-gradient(160deg,#d8b27a,#a57a44)"></div><p>Vapes</p></div>
      <div class="cat"><div class="ph" role="img" aria-label="Photo of colourful hemp gummies with flower buds" style="background:linear-gradient(160deg,#5a4a4a,#b04a5a)"></div><p>Edibles</p></div>
    </div>
    <div class="btn-row"><span class="btn-line">Discover 3500+ Products</span><span class="btn-line">Explore All Categories</span></div>
  </div>
</section>

<section class="standards">
  <h2>Better Standards, Because You Deserve The Best.</h2>
  <div class="std-row">
    <div class="std"><svg width="56" height="56" viewBox="0 0 56 56" fill="none" stroke="#fff" stroke-width="2"><path d="M28 6v44M28 30l-16-8M28 30l16-8M28 38l-12 4M28 38l12 4"/></svg>100% Organic<br>Ingredients</div>
    <div class="std"><svg width="56" height="56" viewBox="0 0 56 56" fill="none" stroke="#fff" stroke-width="2"><path d="M10 28h36a18 14 0 01-36 0z"/><path d="M20 46h16M30 26l10-16"/></svg>Ayurvedic<br>Roots</div>
    <div class="std"><svg width="56" height="56" viewBox="0 0 56 56" fill="none" stroke="#fff" stroke-width="2"><circle cx="28" cy="28" r="18"/><path d="M28 14v28M18 28h20"/></svg>Sourced In<br>The USA</div>
    <div class="std"><svg width="56" height="56" viewBox="0 0 56 56" fill="none" stroke="#fff" stroke-width="2"><rect x="20" y="14" width="16" height="34" rx="3"/><path d="M24 8h8v6"/><path d="M24 30l3 3 6-7"/></svg>Third-Party<br>Lab Tested</div>
    <div class="std"><svg width="56" height="56" viewBox="0 0 56 56" fill="none" stroke="#fff" stroke-width="2"><circle cx="28" cy="18" r="9"/><path d="M12 50c0-12 32-12 32 0"/></svg>Doctor<br>Backed</div>
  </div>
</section>

<section class="products">
  <div class="wrap">
    <h2>Our Products</h2>
    <p class="sub">Elevate your health and wellbeing with our curated collection of hemp-derived products.</p>
    <div class="tabs"><span class="on">All</span><span>THCA Flower</span><span>Concentrates</span><span>Vapes</span><span>Edibles</span></div>
    <div class="prod-row">
      <div class="prod"><div class="ph" role="img" aria-label="Product photo of an amber vape cartridge" style="background:linear-gradient(180deg,#f3f0e6,#d9a84a 60%,#f3f0e6)"></div><div class="stars">★★★★★</div><p>Lorem Ipsum is simply dummy text of the</p><div class="price">$25.99</div></div>
      <div class="prod hot">
        <svg class="mini" style="left:14px" width="26" height="24" viewBox="0 0 28 26" fill="none" stroke="#4d8a4a" stroke-width="2"><path d="M14 23S3 16 3 9a5.5 5.5 0 0111-2 5.5 5.5 0 0111 2c0 7-11 14-11 14z"/></svg>
        <svg class="mini" style="right:14px" width="26" height="24" viewBox="0 0 28 26" fill="none" stroke="#4d8a4a" stroke-width="2"><path d="M2 3h4l3 14h14l3-10H8"/><circle cx="11" cy="22" r="2"/><circle cx="21" cy="22" r="2"/></svg>
        <div class="ph" role="img" aria-label="Product photo of a dried hemp flower bud" style="background:radial-gradient(circle,#7a6a44,#e9f3e8 70%)"></div><div class="stars">★★★★★</div><p>Lorem Ipsum is simply dummy text of the</p><div class="price">$25.99</div><span class="buy">Buy Now</span></div>
      <div class="prod"><div class="ph" role="img" aria-label="Product photo of a silver vape pen" style="background:linear-gradient(135deg,#fff 30%,#b8b8b8 50%,#fff 70%)"></div><div class="stars">★★★★★</div><p>Lorem Ipsum is simply dummy text of the</p><div class="price">$25.99</div></div>
      <div class="prod"><div class="ph" role="img" aria-label="Product photo of colourful hemp gummy cubes with a leaf" style="background:radial-gradient(circle,#e86a3a,#f2c54a 45%,#fff 72%)"></div><div class="stars">★★★★★</div><p>Lorem Ipsum is simply dummy text of the</p><div class="price">$25.99</div></div>
    </div>
  </div>
</section>
<span class="arrow" style="left:75px"><svg width="20" height="12" viewBox="0 0 20 12" fill="none" stroke="#4d8a4a" stroke-width="1.5"><path d="M19 6H1M6 1L1 6l5 5"/></svg></span>
<span class="arrow" style="left:1094px"><svg width="20" height="12" viewBox="0 0 20 12" fill="none" stroke="#4d8a4a" stroke-width="1.5"><path d="M1 6h18M14 1l5 5-5 5"/></svg></span>

<section class="sustain" role="img" aria-label="Misty green mountain range at dusk">
  <div class="ph" role="img" aria-label="Photo of dark green hemp product jars and a dropper bottle" style="background:linear-gradient(160deg,#5e7a5a,#23302a)"></div>
  <div class="sustain-copy">
    <h2>Sustainability</h2>
    <div class="rule"></div>
    <p>Every product on our shelves is sourced in the United States from licensed farms that grow hemp with care for the soil, water and the people who work the land. Before anything reaches you, each batch is third-party lab tested for potency and purity, and the results are posted so you always know exactly what you are getting. Clean, honest hemp, grown close to home and checked by independent labs.</p>
    <span class="btn-soft" style="margin-top:38px">Shop Now</span>
  </div>
</section>

<section class="stories">
  <div class="wrap">
    <p class="kicker">500k+ happy customers</p>
    <h2>Real Stories, Real Relief</h2>
    <div class="story-row">
      <div class="story quote"><div class="qm">“</div><p>Lorem ipsum dolor sit amet, consectetur adipiscing elit, sed do eiusmod tempor incididunt ut labore et dolore magna aliqua. Ut enim ad minim veniam, quis nostrud exercitation ullamco laboris nisi ut aliquip ex ea commodo consequat. Duis aute irure dolor in reprehenderit in voluptate velit esse cillum dolore eu fugiat nulla pariatur.</p><div class="who"><i></i><span>Dana Reyes<br>USA</span></div></div>
      <div class="story" role="img" aria-label="Photo of hands holding a dropper over a tincture bottle" style="background:linear-gradient(160deg,#3a4250,#1e2430)"></div>
      <div class="story quote"><div class="qm">“</div><p>Lorem ipsum dolor sit amet, consectetur adipiscing elit, sed do eiusmod tempor incididunt ut labore et dolore magna aliqua. Ut enim ad minim veniam, quis nostrud exercitation ullamco laboris nisi ut aliquip ex ea commodo consequat. Duis aute irure dolor in reprehenderit in voluptate velit esse cillum dolore eu fugiat nulla pariatur.</p><div class="who"><i></i><span>Dana Reyes<br>USA</span></div></div>
      <div class="story" role="img" aria-label="Photo of a customer holding a hemp plant in cupped hands" style="background:linear-gradient(160deg,#6f8a5a,#2c3a2c)"></div>
    </div>
  </div>
</section>
<span class="arrow" style="left:75px;top:3235px"><svg width="20" height="12" viewBox="0 0 20 12" fill="none" stroke="#4d8a4a" stroke-width="1.5"><path d="M19 6H1M6 1L1 6l5 5"/></svg></span>
<span class="arrow" style="left:1094px;top:3235px"><svg width="20" height="12" viewBox="0 0 20 12" fill="none" stroke="#4d8a4a" stroke-width="1.5"><path d="M1 6h18M14 1l5 5-5 5"/></svg></span>

<section class="news">
  <h2>Stay Updated On All Things Cannabis</h2>
  <p>Join our mailing list and get 10% off on your next order.</p>
  <div class="field">Enter your email<b>JOIN</b></div>
</section>

<footer class="footer">
  <div class="f-logo">Ridgeline<br>Hemp Co.</div>
  <div class="f-col" style="left:398px;width:250px">
    <h4>CONTACT US</h4>
    <div class="f-line"><svg width="12" height="16" viewBox="0 0 12 16" fill="#4a8fbf"><path d="M6 0a6 6 0 016 6c0 4-6 10-6 10S0 10 0 6a6 6 0 016-6z"/><circle cx="6" cy="6" r="2" fill="#fff"/></svg><span>418 Cedar Loop, Ste 2, Alder Falls,<br>MT 59001 USA</span></div>
    <div class="f-line"><svg width="14" height="14" viewBox="0 0 14 14" fill="#4a8fbf"><path d="M3 0l3 3-2 2c1 2 3 4 5 5l2-2 3 3-2 3C6 14 0 8 0 3z"/></svg><span>+1 555 014 2290</span></div>
    <div class="f-line"><svg width="14" height="12" viewBox="0 0 14 12" fill="#4a8fbf"><rect width="14" height="12" rx="1"/><path d="M1 1l6 5 6-5" stroke="#fff" fill="none"/></svg><span>hello@ridgelinehemp.com</span></div>
  </div>
  <div class="f-col" style="left:704px">
    <h4>MENU</h4>
    Home<br>About us<br>Categories<br>Products<br>Blog<br>Shop<br>Contact us
  </div>
  <div class="f-col" style="left:851px">
    <h4>FOLLOW US</h4>
    <div class="socials"><i></i><i></i><i></i><i></i><i></i></div>
    <span class="enquire">ENQUIRE NOW</span>
  </div>
  <div class="copy">Copyright © 2025 All Rights Reserved</div>
</footer>

</body>
</html>
```